8.5 x 8.5 Tobin Marsh Flyer

Wednesday Workouts
with
Tobin Marsh
@liftwithtobinmarsh
Sponsored by ARBOR CREST HOMES GROUP
Join us Virtually each Wednesday from 7 - 7:30 pm
email frontdesk@arborcresthomes.example for MeetRoom Link
reserved for ACHG Agents and Special Invitees
ARBOR CREST HOMES
Phone (555) 812-3367

```html
<!DOCTYPE html>
<html lang="en">
<head>
<meta charset="utf-8">
<title>Wednesday Workouts with Tobin Marsh</title>
<link rel="stylesheet" href="https://fonts.googleapis.com/css2?family=Montserrat:ital,wght@0,300;0,400;0,500;0,600;0,700;1,500;1,800;1,900&display=swap">
<style>
  :root {
    --stage: #8a8b8f;
    --ink-dark: #1e1f21;
    --gym-grey: #3a3b3d;
    --teal: #0f6f86;
    --teal-deep: #0b4a5c;
    --teal-bright: #1b8fa3;
    --white: #ffffff;
    --band: rgba(18, 28, 30, 0.82);
  }
  html, body {
    margin: 0;
    padding: 0;
    width: 1200px;
    height: 1178px;
    overflow: hidden;
    background: var(--stage);
    font-family: "Montserrat", sans-serif;
  }
  .flyer {
    position: absolute;
    left: 127px;
    top: 116px;
    width: 946px;
    height: 946px;
    overflow: hidden;
    background: var(--ink-dark);
    color: var(--white);
    box-shadow: 0 2px 6px rgba(0,0,0,0.25);
  }
  .flyer-backdrop {
    position: absolute;
    inset: 0;
    width: 100%;
    height: 100%;
  }
  .headline {
    position: absolute;
    left: 47px;
    margin: 0;
    font-style: italic;
    font-weight: 900;
    line-height: 1;
    text-shadow: 3px 4px 8px rgba(0,0,0,0.45);
  }
  .headline-day { top: 146px; font-size: 70px; }
  .headline-main { top: 218px; font-size: 104px; letter-spacing: -2px; }
  .with {
    position: absolute;
    left: 225px;
    top: 338px;
    font-size: 50px;
    font-weight: 300;
    line-height: 1;
  }
  .trainer-name {
    position: absolute;
    left: 66px;
    top: 386px;
    margin: 0;
    font-size: 80px;
    font-weight: 300;
    line-height: 1;
    text-shadow: 2px 3px 6px rgba(0,0,0,0.4);
  }
  .handle-bar {
    position: absolute;
    left: 0;
    top: 498px;
    width: 447px;
    height: 53px;
    background: var(--white);
    clip-path: polygon(0 0, 100% 0, 93% 100%, 0 100%);
  }
  .handle {
    position: absolute;
    left: 40px;
    top: 12px;
    font-size: 23px;
    font-weight: 500;
    font-style: italic;
    letter-spacing: 5.4px;
    color: var(--teal);
  }
  .details {
    position: absolute;
    top: 600px;
    font-size: 24px;
    font-weight: 600;
    line-height: 30px;
  }
  .details-when { left: 47px; }
  .details-contact {
    left: 277px;
    padding-left: 14px;
    border-left: 2px solid var(--white);
  }
  .info-band {
    position: absolute;
    left: 0;
    top: 766px;
    width: 100%;
    height: 139px;
    background: var(--band);
  }
  .brand-name {
    position: absolute;
    left: 54px;
    top: 864px;
    width: 380px;
    font-size: 28px;
    font-weight: 500;
    line-height: 1.2;
    white-space: nowrap;
  }
  .sponsor {
    position: absolute;
    left: 465px;
    top: 776px;
    width: 440px;
  }
  .reserved {
    font-size: 18px;
    font-weight: 400;
    padding-bottom: 3px;
    border-bottom: 2px solid var(--white);
    white-space: nowrap;
  }
  .sponsored {
    margin-top: 10px;
    font-size: 22px;
    font-weight: 400;
    white-space: nowrap;
  }
  .sponsored strong { font-weight: 700; }
  .phone {
    margin-top: 2px;
    font-size: 48px;
    font-weight: 700;
    line-height: 1.1;
    white-space: nowrap;
  }
</style>
</head>
<body>
  <main class="flyer">
    <svg class="flyer-backdrop" viewBox="0 0 946 946" role="img" aria-label="Photo of the trainer in a tank top and headband standing with a barbell, over a dimmed gym equipment backdrop">
      <defs>
        <linearGradient id="gymShade" x1="0" y1="0" x2="1" y2="1">
          <stop offset="0" stop-color="#3b3c3e"/>
          <stop offset="1" stop-color="#1f2022"/>
        </linearGradient>
        <linearGradient id="tealPanel" x1="0" y1="0" x2="0" y2="1">
          <stop offset="0" stop-color="#0d5468"/>
          <stop offset="1" stop-color="#10728a"/>
        </linearGradient>
        <radialGradient id="figure" cx="0.5" cy="0.45" r="0.55">
          <stop offset="0" stop-color="#6a4a38"/>
          <stop offset="0.6" stop-color="#2b3a44"/>
          <stop offset="1" stop-color="#0d5468" stop-opacity="0"/>
        </radialGradient>
      </defs>
      <rect width="946" height="946" fill="url(#gymShade)"/>
      <polygon points="561,0 946,0 946,946 265,946" fill="url(#tealPanel)"/>
      <ellipse cx="735" cy="520" rx="250" ry="470" fill="url(#figure)"/>
    </svg>

    <h1 class="headline headline-day">Wednesday</h1>
    <div class="headline headline-main">Workouts</div>
    <div class="with">with</div>
    <h2 class="trainer-name">Tobin Marsh</h2>

    <div class="handle-bar"><span class="handle">@liftwithtobinmarsh</span></div>

    <div class="details details-when">Join us Virtually<br>each Wednesday<br>from 7 - 7:30 pm</div>
    <div class="details details-contact">email<br>frontdesk@arborcresthomes.example<br>for MeetRoom Link</div>

    <div class="info-band"></div>
    <div class="brand-name">ARBOR CREST HOMES</div>
    <div class="sponsor">
      <div class="reserved">reserved for ACHG Agents and Special Invitees</div>
      <div class="sponsored">Sponsored by: <strong>ARBOR CREST HOMES</strong></div>
      <div class="phone">Ph: (555) 812-3367</div>
    </div>
  </main>
</body>
</html>
```